'Tarvel' a financial/crypto-currency exchange in the middle east

On the card we need 1) Name 2) title 3) email address 4) phone number using the same colors and theme as the logo. On one side we just want the logo and we want the whole card to be in blue (same blue as logo) with the logo in the back being white.
Industry/Entity Type
Financial

```html
<!DOCTYPE html>
<html lang="en">
<head>
<meta charset="UTF-8">
<title>Tarvel – Business Card</title>
<link rel="stylesheet" href="https://fonts.googleapis.com/css2?family=Lato:wght@400;700;900&display=swap">
<style>
  :root {
    --brand-blue: #1a8fce;
    --ink: #1f1f1f;
    --card-white: #ffffff;
    --backdrop: #eceef0;
  }
  html, body {
    margin: 0;
    padding: 0;
    width: 1200px;
    height: 900px;
    overflow: hidden;
    background: var(--backdrop);
    font-family: "Lato", Arial, sans-serif;
  }
  .business-card {
    position: absolute;
    left: 275px;
    top: 250px;
    width: 650px;
    height: 400px;
    background: var(--card-white);
    border-radius: 200px 0 0 200px;
    box-shadow: 0 10px 30px rgba(0, 0, 0, 0.12);
  }
  .holder {
    position: absolute;
    right: 32px;
    top: 54px;
    text-align: right;
  }
  .holder-name {
    margin: 0;
    font-size: 22px;
    font-weight: 700;
    letter-spacing: 0.3px;
    color: var(--brand-blue);
    line-height: 1.1;
  }
  .holder-title {
    margin: 4px 0 0;
    font-size: 17px;
    font-weight: 400;
    color: var(--ink);
  }
  .brand {
    position: absolute;
    left: 43px;
    top: 138px;
    display: flex;
    align-items: center;
    gap: 24px;
  }
  .brand-mark {
    width: 120px;
    height: 120px;
    border-radius: 50%;
    border: 4px solid var(--brand-blue);
    box-sizing: border-box;
  }
  .brand-name {
    font-size: 70px;
    font-weight: 900;
    color: var(--brand-blue);
    letter-spacing: 0.5px;
    line-height: 1;
  }
  .contact-list {
    position: absolute;
    right: 32px;
    top: 280px;
    margin: 0;
    padding: 0;
    list-style: none;
  }
  .contact-item {
    display: flex;
    justify-content: flex-end;
    align-items: center;
    gap: 6px;
    height: 24.5px;
    font-size: 17px;
    color: var(--ink);
  }
  .contact-icon {
    width: 22px;
    height: 22px;
    flex: none;
  }
</style>
</head>
<body>
  <div class="business-card">
    <div class="holder">
      <h1 class="holder-name">DANIEL HARPER</h1>
      <p class="holder-title">Managing Director</p>
    </div>

    <div class="brand">
      <div class="brand-mark"></div>
      <span class="brand-name">Tarvel</span>
    </div>

    <ul class="contact-list">
      <li class="contact-item">
        <span>444 555 7120</span>
        <svg class="contact-icon" viewBox="0 0 22 22" aria-hidden="true">
          <circle cx="11" cy="11" r="10" fill="none" stroke="var(--brand-blue)" stroke-width="1.4"/>
          <circle cx="11" cy="11" r="7.5" fill="var(--brand-blue)"/>
          <path d="M7.6 8.2c.3 3 2.6 5.6 5.8 6.2l1-1.3-1.6-1-.8.7c-1-.5-1.8-1.3-2.3-2.3l.7-.8-1-1.6z" fill="#fff"/>
        </svg>
      </li>
      <li class="contact-item">
        <span>info@tarvelx.com</span>
        <svg class="contact-icon" viewBox="0 0 22 22" aria-hidden="true">
          <circle cx="11" cy="11" r="10" fill="none" stroke="var(--brand-blue)" stroke-width="1.4"/>
          <circle cx="11" cy="11" r="7.5" fill="var(--brand-blue)"/>
          <rect x="7" y="8.3" width="8" height="5.6" fill="#fff"/>
          <path d="M7 8.3l4 3.2 4-3.2" fill="none" stroke="var(--brand-blue)" stroke-width="0.9"/>
        </svg>
      </li>
      <li class="contact-item">
        <span>www.tarvelx.com</span>
        <svg class="contact-icon" viewBox="0 0 22 22" aria-hidden="true">
          <circle cx="11" cy="11" r="10" fill="none" stroke="var(--brand-blue)" stroke-width="1.4"/>
          <circle cx="11" cy="11" r="7.5" fill="var(--brand-blue)"/>
          <circle cx="11" cy="11" r="4.2" fill="none" stroke="#fff" stroke-width="1"/>
          <ellipse cx="11" cy="11" rx="1.8" ry="4.2" fill="none" stroke="#fff" stroke-width="0.9"/>
          <line x1="6.8" y1="11" x2="15.2" y2="11" stroke="#fff" stroke-width="0.9"/>
        </svg>
      </li>
    </ul>
  </div>
</body>
</html>
```